Industrial Project Sign

We need an eye catching (but professional) industrial project sign that will be very large (roughly 12' high x 18' wide). This sign will be highly visible from the adjacent high speed highway.

* The following needs to be at the bottom of the signage: Logo (uploaded), Name (Pillar Ventures Group, Inc.) (uploaded) and phone number (555)613-8874

*Name of Project - "Brambleford Industrial Center"

* Text items
Land for Sale
Build to Suit
Zoning: Industrial (G I & L I)

* Interesting background that is eye catching
Updates

Good morning all,

We are considering all designers options as we go and are waiting for the final designs to come in by the 4th so that we can give each one a good look.   If you have any new designs, questions, further design options or any tweeks you want to do to current designs, please do so at this time.

Thanks to all of you for your submissions.

Industry/Entity Type

Industrial

```html
<!DOCTYPE html>
<html lang="en">
<head>
<meta charset="utf-8">
<title>Brambleford Industrial Center – Project Sign</title>
<link rel="stylesheet" href="https://fonts.googleapis.com/css2?family=Barlow+Condensed:wght@600&family=Barlow+Semi+Condensed:wght@500;600;700&display=swap">
<style>
  :root {
    --maroon: #630c10;
    --amber: #f9a84b;
    --white: #ffffff;
  }
  * { margin: 0; padding: 0; box-sizing: border-box; }
  html, body {
    width: 1200px;
    height: 800px;
    overflow: hidden;
    background: var(--maroon);
  }
  .sign {
    position: relative;
    width: 1200px;
    height: 800px;
    background: var(--maroon);
    font-family: "Barlow Semi Condensed", "Arial Narrow", sans-serif;
  }
  .brand-mark {
    position: absolute;
    top: 100px;
    right: 40px;
    width: 150px;
    display: flex;
    flex-direction: column;
    align-items: center;
    gap: 18px;
  }
  .brand-mark__square {
    width: 70px;
    height: 70px;
    background: var(--white);
  }
  .brand-mark__name {
    color: var(--white);
    font-weight: 700;
    font-size: 38px;
    letter-spacing: 1px;
  }
  .project-title {
    position: absolute;
    left: 46px;
    top: 210px;
    color: var(--amber);
    font-family: "Barlow Condensed", "Arial Narrow", sans-serif;
    font-weight: 600;
    font-size: 128px;
    line-height: 99px;
    letter-spacing: 4px;
    text-transform: uppercase;
  }
  .features {
    position: absolute;
    left: 455px;
    top: 418px;
    list-style: none;
    color: var(--white);
    font-weight: 600;
    font-size: 38px;
    line-height: 46.5px;
    letter-spacing: 1.5px;
    text-transform: uppercase;
  }
  .features li { display: flex; align-items: center; }
  .features__marker {
    width: 18px;
    height: 22px;
    margin-right: 14px;
    flex-shrink: 0;
  }
  .contact-band {
    position: absolute;
    left: 0;
    top: 632px;
    width: 1200px;
    height: 146px;
    background: var(--amber);
  }
  .company {
    position: absolute;
    left: 40px;
    top: 48px;
    display: flex;
    align-items: center;
    gap: 14px;
  }
  .company__square {
    width: 62px;
    height: 62px;
    background: var(--maroon);
  }
  .company__name {
    color: var(--maroon);
    font-weight: 700;
    font-size: 17px;
    padding-bottom: 5px;
    border-bottom: 2px solid var(--maroon);
  }
  .company__web {
    color: var(--maroon);
    font-weight: 500;
    font-size: 13px;
    margin-top: 4px;
  }
  .contact-line {
    position: absolute;
    left: 370px;
    top: 32px;
    color: var(--maroon);
    font-weight: 600;
    font-size: 64px;
    letter-spacing: 1px;
    text-transform: uppercase;
    white-space: nowrap;
  }
</style>
</head>
<body>
<main class="sign">
  <div class="brand-mark">
    <div class="brand-mark__square"></div>
    <div class="brand-mark__name">PILLAR</div>
  </div>

  <h1 class="project-title">Brambleford<br>Industrial<br>Center</h1>

  <ul class="features">
    <li><svg class="features__marker" viewBox="0 0 18 22"><path d="M9 2 L16 11 L9 20 L2 11 Z" fill="none" stroke="#ffffff" stroke-width="3"/></svg>Land for Sale</li>
    <li><svg class="features__marker" viewBox="0 0 18 22"><path d="M9 2 L16 11 L9 20 L2 11 Z" fill="none" stroke="#ffffff" stroke-width="3"/></svg>Build to Suit</li>
    <li><svg class="features__marker" viewBox="0 0 18 22"><path d="M9 2 L16 11 L9 20 L2 11 Z" fill="none" stroke="#ffffff" stroke-width="3"/></svg>Zoning: Industrial (G I &amp; L I)</li>
  </ul>

  <footer class="contact-band">
    <div class="company">
      <div class="company__square"></div>
      <div>
        <div class="company__name">Pillar Ventures Group, Inc.</div>
        <div class="company__web">www.pillarventuresgroup.com</div>
      </div>
    </div>
    <p class="contact-line">Contact us at (555)613-8874</p>
  </footer>
</main>
</body>
</html>
```